Cover design required for our new homes catalogue

Tidewell Houses build new prefabricated homes in New Zealand.
Our smart building system means we can supply houses at affordable prices and deliver them all over New Zealand.
The catalogue content tells customers about our company and shows them our range of house designs.
The cover needs to be inviting and professional.
Our main company colour is Pantone Blue 3005.
Secondary colours are Pantone dark blue 302 & Grey (40% black).

I'll upload a copy of our old catalogue cover & some new pictures - we want a different layout but similar content, just new pictures.

Target Market(s)

Professional people wanting a new home, holiday home, farm home, rural homes, small homes, prefabricated office buildings, tourist accommodation

Industry/Entity Type

Residential Construction

Font styles to use
Sans Serif

Colors
0692cd

Requirements
Must have
• Our logo & Tagline "Smart affordable homes".
Nice to have
• Pictures of our homes & scenery

```html
<!DOCTYPE html>
<html lang="en">
<head>
<meta charset="utf-8">
<title>Tidewell Houses – Homes Catalogue Cover</title>
<link rel="stylesheet" href="https://fonts.googleapis.com/css2?family=Open+Sans:wght@300;400;700;800&display=swap">
<style>
  :root {
    --backdrop: #e2e7ea;
    --brand-blue: #0784c8;
    --sky-blue: #25a8dd;
    --ink-blue: #0d6da6;
    --panel-grey: #e9e9e9;
    --panel-white: #f7f7f7;
    --paper: #ffffff;
  }
  html, body {
    margin: 0;
    width: 1200px;
    height: 1030px;
    overflow: hidden;
    background: var(--backdrop);
  }
  .canvas {
    position: relative;
    width: 1200px;
    height: 1030px;
  }
  .catalogue-cover {
    position: absolute;
    left: 260px;
    top: 35px;
    width: 680px;
    height: 960px;
    box-shadow: 0 10px 28px rgba(40, 60, 70, 0.25);
    background: var(--paper);
  }
  .catalogue-cover svg { display: block; }
  .brand-name {
    font-family: "Open Sans", Arial, sans-serif;
    font-weight: 700;
    font-size: 40px;
    fill: var(--paper);
  }
  .issue-date, .issue-title {
    font-family: "Open Sans", Arial, sans-serif;
    font-size: 24px;
    fill: var(--ink-blue);
  }
  .issue-date { font-weight: 300; }
  .issue-title .light { font-weight: 300; }
  .issue-title .strong { font-weight: 800; }
  .tagline {
    font-family: "Open Sans", Arial, sans-serif;
    font-weight: 700;
    font-size: 24px;
    fill: var(--paper);
  }
</style>
</head>
<body>
<div class="canvas">
  <div class="catalogue-cover">
    <svg width="680" height="960" viewBox="0 0 680 960" xmlns="http://www.w3.org/2000/svg">
      <defs>
        <linearGradient id="tree-tones" x1="0" y1="0" x2="0.6" y2="1">
          <stop offset="0" stop-color="#d99a2a"/>
          <stop offset="0.45" stop-color="#f2d27a"/>
          <stop offset="0.75" stop-color="#8fa25a"/>
          <stop offset="1" stop-color="#4f8a2a"/>
        </linearGradient>
        <linearGradient id="deck-tones" x1="0" y1="0" x2="0.3" y2="1">
          <stop offset="0" stop-color="#3f6a3c"/>
          <stop offset="0.35" stop-color="#2f3c4e"/>
          <stop offset="0.65" stop-color="#a58a6c"/>
          <stop offset="1" stop-color="#7a6450"/>
        </linearGradient>
        <linearGradient id="kitchen-tones" x1="0" y1="0" x2="0" y2="1">
          <stop offset="0" stop-color="#f4f5f6"/>
          <stop offset="0.7" stop-color="#d5d8db"/>
          <stop offset="1" stop-color="#6c6a68"/>
        </linearGradient>
        <linearGradient id="house-tones" x1="0" y1="0" x2="0" y2="1">
          <stop offset="0" stop-color="#7fb9e8"/>
          <stop offset="0.2" stop-color="#4a4d52"/>
          <stop offset="0.55" stop-color="#2c2e31"/>
          <stop offset="0.72" stop-color="#5a5a58"/>
          <stop offset="1" stop-color="#3f8a22"/>
        </linearGradient>
      </defs>

      <rect class="cover-paper" width="680" height="960" fill="var(--panel-white)"/>

      <polygon class="photo-scenery" role="img" aria-label="Autumn tree over a sunlit green hillside"
               points="0,0 112,0 318,214 140,420 0,436" fill="url(#tree-tones)"/>

      <polygon class="masthead-band" points="132,0 680,0 680,36 436,318" fill="var(--brand-blue)"/>

      <polygon class="photo-deck" role="img" aria-label="Prefabricated home with open kitchen and timber deck"
               points="680,70 680,560 470,350" fill="url(#deck-tones)"/>

      <polygon class="issue-panel" points="150,450 305,285 480,440 325,610" fill="var(--panel-grey)"/>

      <polygon class="photo-kitchen" role="img" aria-label="Bright white kitchen interior with pot plant"
               points="370,625 470,525 570,620 470,720" fill="url(#kitchen-tones)"/>

      <polygon class="photo-house" role="img" aria-label="Modern dark clad home with deck and lawn"
               points="0,466 126,452 430,742 250,960 0,960" fill="url(#house-tones)"/>

      <polygon class="tagline-band" points="680,600 680,960 320,960" fill="var(--sky-blue)"/>

      <g class="brand-lockup">
        <rect x="222" y="74" width="34" height="34" fill="var(--paper)"/>
        <text class="brand-name" x="270" y="106">Tidewell Houses</text>
      </g>

      <g class="issue-heading">
        <text class="issue-date" x="195" y="432">AUG 2016</text>
        <text class="issue-title" x="195" y="460"><tspan class="light">HOMES </tspan><tspan class="strong">CATALOGUE</tspan></text>
      </g>

      <g class="tagline">
        <text x="450" y="868">SMART</text>
        <text x="450" y="898">PREFABRICATED</text>
        <text x="450" y="928">HOMES</text>
      </g>
    </svg>
  </div>
</div>
</body>
</html>
```